Packaging Design Project

THIS IS A PRODUCT THAT IS SOLD IN SMOKE SHOPS AND HEAD SHOPS IT IS CALLED GOLDEN MEADOW IT WILL BE SOLD IN A 2 DRAM BLUE BOTTLE WITH A SILVER CAP BELOW IN FILES IS A SAMPLE OF THE WORDING I NEED ON THE BOOTLE ALSO I NEED TO ADD SOMETHING LIKE POWERED BY KRATOM IS THE MAIN INGREDIENT
Updates
i uploade a picture of bootle thanks
Industry/Entity Type
Product
Look and feel
Each slider illustrates characteristics of the customer's brand and the style your logo design should communicate.

```html
<!DOCTYPE html>
<html lang="en">
<head>
<meta charset="utf-8">
<title>Golden Meadow – Kratom Liquid Mood Enhancer Label</title>
<link rel="stylesheet" href="https://fonts.googleapis.com/css2?family=Roboto:wght@300;900&family=Montserrat:wght@200&display=swap">
<style>
  :root {
    --ink-black: #000000;
    --deep-blue: #0a2a7a;
    --glow-blue: #2a5bd0;
    --white: #ffffff;
    --ring-grey: #9a9a9a;
  }
  html, body {
    margin: 0;
    padding: 0;
    width: 1016px;
    height: 1200px;
    overflow: hidden;
    background: var(--ink-black);
  }
  .label {
    position: relative;
    width: 1016px;
    height: 1200px;
    overflow: hidden;
    background:
      radial-gradient(ellipse 640px 480px at 508px 280px, var(--glow-blue) 0%, var(--deep-blue) 40%, rgba(5,15,50,0.6) 68%, var(--ink-black) 100%);
  }
  .brand {
    position: absolute;
    left: 0;
    right: 0;
    margin: 0;
    text-align: center;
    font-family: "Roboto", sans-serif;
    font-weight: 900;
    line-height: 1;
    letter-spacing: 2px;
    color: var(--white);
  }
  .brand-line-one { top: 77px; font-size: 148px; }
  .brand-line-two { top: 218px; font-size: 180px; }
  .tagline {
    position: absolute;
    top: 383px;
    left: 0;
    right: 0;
    margin: 0;
    text-align: center;
    font-family: "Roboto", sans-serif;
    font-weight: 900;
    font-size: 21px;
    letter-spacing: 0.5px;
    color: var(--white);
  }
  .ingredient-seal {
    position: absolute;
    box-sizing: border-box;
    left: 306px;
    top: 569px;
    width: 404px;
    height: 404px;
    border-radius: 50%;
    background: var(--ink-black);
    border: 3px solid var(--ring-grey);
    display: flex;
    flex-direction: column;
    align-items: center;
    justify-content: center;
    color: var(--white);
    font-family: "Roboto", sans-serif;
    font-weight: 300;
  }
  .ingredient-name {
    font-size: 82px;
    line-height: 1;
    letter-spacing: 1px;
  }
  .ingredient-strength {
    margin-top: 8px;
    font-size: 31px;
    letter-spacing: 1px;
  }
  .product-type {
    position: absolute;
    top: 1014px;
    left: 0;
    right: 0;
    margin: 0;
    text-align: center;
    font-family: "Montserrat", sans-serif;
    font-weight: 200;
    font-size: 76px;
    line-height: 73px;
    letter-spacing: 2px;
    color: var(--white);
  }
</style>
</head>
<body>
  <main class="label">
    <h1 class="brand brand-line-one">GOLDEN</h1>
    <h1 class="brand brand-line-two">MEADOW</h1>

    <p class="tagline">CHEMICAL FREE - ADVANCED EXTRACTION METHODS</p>

    <div class="ingredient-seal">
      <span class="ingredient-name">KRATOM</span>
      <span class="ingredient-strength">MAXIMUM POTENCY</span>
    </div>

    <p class="product-type">LIQUID MOOD<br>ENHANCER</p>
  </main>
</body>
</html>
```